Graphic Design for a Info Card

We would like a graphic design for an info card . We would like the colours to correspond to our logo , you can add in the colours navy blue or yellow if you would like. We would like it to have the following information. We want something that really pops. We would like the size to be 4 1/2 x 6 .

ATTENTION!! Delivery Promo! Order from us on the @hopplemeals app or @marlinrunner app on FRIDAYS and receive a FREE Sample of our one of our meal prep meals in your bag!
DID YOU KNOW?! Meal Prep is another great service that we offer. Saving you time, promoting your health, and best of all providing a delicious lunch . You can find more info on our website www.brivoranpantry.example . All orders are available for delivery or pickup!

```html
<!DOCTYPE html>
<html lang="en">
<head>
<meta charset="utf-8">
<title>Brivoran Delivery Promo Card</title>
<link rel="stylesheet" href="https://fonts.googleapis.com/css2?family=Kaushan+Script&family=Poppins:wght@400;500;600;700;800&display=swap">
<style>
  :root {
    --royal: #1f2fa3;
    --royal-deep: #101a72;
    --royal-light: #3b52c8;
    --navy-text: #1b2a8c;
    --ink: #1a1a2e;
    --lime: #b6d335;
    --red: #d8141d;
    --white: #ffffff;
  }
  * { box-sizing: border-box; margin: 0; padding: 0; }
  html, body { width: 900px; height: 1200px; overflow: hidden; background: var(--royal-deep); }
  .card {
    position: relative; width: 900px; height: 1200px; overflow: hidden;
    background: radial-gradient(ellipse at 50% 45%, var(--royal) 0%, var(--royal) 55%, var(--royal-deep) 100%);
    font-family: "Poppins", sans-serif;
  }
  .strokes { position: absolute; inset: 0; }
  .brand { position: absolute; top: 34px; right: 48px; }
  .brand-name { font-size: 50px; font-weight: 700; color: var(--lime); letter-spacing: 1px; line-height: 1; }
  .brand-tag { font-size: 15px; font-weight: 600; color: var(--lime); margin-top: 6px; letter-spacing: .3px; }
  .attention {
    position: absolute; left: 108px; top: 72px; font-family: "Kaushan Script", cursive; font-weight: 400;
    font-size: 72px; line-height: 1.2; color: var(--red); transform: rotate(-5deg); transform-origin: left center;
  }
  .promo {
    position: absolute; left: 52px; top: 232px; font-size: 64px; font-weight: 800; color: var(--white);
    line-height: 1.0; transform: rotate(-7deg); transform-origin: left top;
  }
  .promo span { display: block; padding-left: 100px; }
  .photo { position: absolute; }
  .photo-sandwich {
    left: 430px; top: 145px; width: 465px; height: 320px; border-radius: 8px;
    background: linear-gradient(135deg, #d9b07a 0%, #8a5a3a 45%, #5a3a2a 70%, #e8d8c0 100%);
  }
  .photo-mealprep {
    left: 36px; top: 775px; width: 395px; height: 330px;
    background: linear-gradient(160deg, #2a2a2a 0%, #6b4a34 40%, #d9c9a0 65%, #1c1c1c 100%);
  }
  .offer-line { position: absolute; white-space: nowrap; }
  .offer-lead { left: 0; width: 900px; text-align: center; top: 508px; font-size: 37px; font-weight: 700; color: var(--navy-text); line-height: 1.2; }
  .offer-apps { left: 148px; top: 556px; font-size: 22.5px; font-weight: 500; color: var(--ink); line-height: 1.2; }
  .offer-receive { left: 250px; top: 590px; font-size: 24px; font-weight: 500; color: var(--ink); line-height: 1.2; }
  .offer-receive strong { font-size: 46px; font-weight: 700; color: var(--red); }
  .offer-meal { left: 250px; width: 550px; text-align: center; top: 646px; font-size: 28px; font-weight: 500; color: var(--royal); line-height: 1.25; }
  .info { position: absolute; left: 470px; top: 778px; width: 415px; color: var(--white); }
  .info-head { display: flex; align-items: center; gap: 14px; }
  .info-title { font-size: 26px; font-weight: 800; color: var(--lime); text-decoration: underline; text-underline-offset: 4px; }
  .info-body { font-size: 25px; font-weight: 700; line-height: 1.3; margin-top: 8px; }
  .benefits { list-style: none; margin-top: 10px; font-size: 21px; font-weight: 400; }
  .benefits li { display: flex; align-items: center; gap: 10px; line-height: 1.3; }
  .benefits li::before { content: ""; width: 12px; height: 12px; border-radius: 50%; background: var(--lime); flex: none; }
  .benefits .highlight { font-weight: 700; color: var(--lime); }
  .more { position: absolute; right: 32px; top: 1024px; text-align: right; line-height: 1.15; }
  .more-label { font-size: 29px; font-weight: 500; color: var(--navy-text); }
  .more-url { font-size: 29px; font-weight: 700; color: var(--red); }
  .footer { position: absolute; left: 0; top: 1126px; width: 900px; display: flex; justify-content: center; align-items: center; gap: 18px; }
  .footer-text { font-size: 22.5px; font-weight: 400; color: var(--lime); }
</style>
</head>
<body>
<main class="card">
  <svg class="strokes" width="900" height="1200" viewBox="0 0 900 1200" aria-hidden="true">
    <path d="M0 20 L330 0 L300 30 L0 60 Z" fill="var(--royal-light)" opacity=".5"/>
    <path d="M820 120 L900 90 L900 260 L860 240 Z" fill="var(--white)" opacity=".6"/>
    <path d="M0 720 L120 700 L90 760 L0 770 Z" fill="var(--white)" opacity=".4"/>
    <path d="M860 780 L900 760 L900 1000 L870 960 Z" fill="var(--white)" opacity=".45"/>
    <path d="M62 110 L500 64 L520 84 L490 150 L470 190 L70 208 L90 170 L60 150 Z" fill="var(--lime)"/>
    <path d="M0 470 L230 455 L520 470 L900 450 L900 745 L600 760 L300 748 L0 765 Z" fill="var(--white)"/>
    <path d="M0 455 L160 440 L140 470 L0 480 Z" fill="var(--white)" opacity=".6"/>
    <path d="M440 1040 L880 1005 L900 1015 L890 1092 L450 1110 L470 1072 Z" fill="var(--lime)"/>
    <g stroke="var(--lime)" stroke-width="7" stroke-linecap="round">
      <line x1="405" y1="222" x2="440" y2="208"/>
      <line x1="400" y1="242" x2="462" y2="236"/>
      <line x1="52" y1="334" x2="112" y2="324"/>
      <line x1="68" y1="356" x2="118" y2="350"/>
    </g>
  </svg>

  <div class="brand">
    <div class="brand-name">BRIVORAN</div>
    <div class="brand-tag">HEALTHY KITCHEN | MEAL PREP</div>
  </div>

  <h1 class="attention">Attention!</h1>

  <div class="photo photo-sandwich" role="img" aria-label="Photo of a grilled steak and cheese sandwich cut in half on parchment paper"></div>

  <h2 class="promo">Delivery <span>Promo!</span></h2>

  <section class="offer">
    <p class="offer-line offer-lead">Order from us on FRIDAYS</p>
    <p class="offer-line offer-apps">on the @hopplemeals app or @marlinrunner app</p>
    <p class="offer-line offer-receive">and Receive a <strong>FREE Sample</strong></p>
    <p class="offer-line offer-meal">of our one of our meal prep<br>meals in your bag!</p>
  </section>

  <div class="photo photo-mealprep" role="img" aria-label="Photo of meal prep containers with grilled steak, chicken, rice and vegetables"></div>

  <section class="info">
    <div class="info-head">
      <svg width="32" height="32" viewBox="0 0 24 24" aria-hidden="true"><path d="M12 2 L14.9 8.6 L22 9.3 L16.6 14 L18.2 21 L12 17.3 L5.8 21 L7.4 14 L2 9.3 L9.1 8.6 Z" fill="none" stroke="var(--lime)" stroke-width="1.8"/></svg>
      <span class="info-title">DID YOU KNOW?!</span>
      <svg width="32" height="32" viewBox="0 0 24 24" aria-hidden="true"><path d="M12 2 L14.9 8.6 L22 9.3 L16.6 14 L18.2 21 L12 17.3 L5.8 21 L7.4 14 L2 9.3 L9.1 8.6 Z" fill="none" stroke="var(--lime)" stroke-width="1.8"/></svg>
    </div>
    <p class="info-body">Meal Prep is another great service that we offer.</p>
    <ul class="benefits">
      <li>Saving you time</li>
      <li>Promoting your health</li>
      <li class="highlight">Providing a delicious lunch</li>
    </ul>
  </section>

  <div class="more">
    <p class="more-label">More info on</p>
    <p class="more-url">brivoranpantry.example</p>
  </div>

  <footer class="footer">
    <svg width="36" height="24" viewBox="0 0 36 24" aria-hidden="true"><g stroke="var(--white)" stroke-width="3" stroke-linecap="round"><line x1="4" y1="6" x2="30" y2="3"/><line x1="8" y1="13" x2="32" y2="12"/><line x1="4" y1="20" x2="28" y2="21"/></g></svg>
    <p class="footer-text">All orders are available for delivery or pickup!</p>
    <svg width="36" height="24" viewBox="0 0 36 24" aria-hidden="true"><g stroke="var(--white)" stroke-width="3" stroke-linecap="round"><line x1="6" y1="3" x2="32" y2="6"/><line x1="4" y1="12" x2="28" y2="13"/><line x1="8" y1="21" x2="32" y2="20"/></g></svg>
  </footer>
</main>
</body>
</html>
```